Guaranteed Job - Sleek Sexy Business Card UV Spot

Im looking for a sleek and sexy business card, that resembles elite or VIP status status.
our business is corinvale.example
you can view our products on there, but our main audience for handing out our cards will be for people in the hospitality industry, so it will need to impress high management and CEO of hotels and restaurants, bars, clubs etc...
the card features will have UV spot on both sides, 400gsm stock. standard size.
Artwork should be 86 x 54mm + 2mm bleed = 90 x 58mm
it should have a nice "unique" uv spot pattern that highlights the card, not a repeated pattern, theres no originality there, and it will be disregarded.
The written material will be:
Corin Vale Hospitality College (logo)
Tobin Marsh
Director
Phone: 1300 615 737
Mobile: 0455 817 296
Email: info@corinvale.example
website: www.corinvale.example
I'm looking for originality here, i don't want just a simple stock card, want something that has a wow factor for people.
You will find the logo attached. you may invert the white to black words to suit the background as you please.
thank you and good luck
As a side note, ive received a lot of proposals, im too busy to give feedback to each and every one, so if i havent provided feedback for your design within 24 hours, then consider it not acceptable, and you could resubmit another design.
So far i have not seen any design that stood out for me, they all seem pretty generic. there nothing thats unique, i would figure for the amount that im offering, that people would put some more effort and creativity into the design.
so far over 200 designs submitted, and nothing i have seen looks very original, everything looks like a different variation of the same stuff, i said it very clearly i wanted something unique, the only thing that has come close to it so far is this one
Reason: Ive received alot of design concepts and i have reviewed everyone, but i havent had time to give feedback to every single one, only the ones that have interested me, if i havent responded, its because i havent found it good enough.
so far only a few design have been on par with what ive been looking for, an attractive eye popping design.
heres a few of them,
http://files.pixelbazaar.example/design_img/51736/62418/62418_2840915_51736_image.jpg
http://files.pixelbazaar.example/design_img/51736/68254/68254_2841377_51736_image.jpg
theyre, both unique and original, and eye catching, the only thing theyre missing is the sexyness.
if you still think you have some creativity left in your minds, then throw it on here.
Reason: Sorry guys for the delay, I was in a serious accident and out of commission for the past few months, I'm just slowly recovering now, please bare with me as i try to attend to this project, it may take me awhile as I have other projects that are on standby, I'm not 100% at the moment, so im extending the deadline for 2 weeks right now. Thanks for your patience.
Hospitality

```html
<!DOCTYPE html>
<html lang="en">
<head>
<meta charset="utf-8">
<title>Corin Vale Hospitality College – Business Card</title>
<link rel="stylesheet" href="https://fonts.googleapis.com/css2?family=Montserrat:wght@400;600;700&display=swap">
<style>
  :root {
    --page: #2b2b2e;
    --card-black: #0d0d0f;
    --card-charcoal: #1c1c1f;
    --card-grey: #3a3b3e;
    --sky: #7fb6e0;
    --sky-deep: #4f8cc0;
    --sky-pale: #a9d3f2;
    --text-light: #e6e8ea;
    --text-muted: #a7abaf;
    --logo-panel: #5b5d60;
  }
  * { box-sizing: border-box; margin: 0; padding: 0; }
  html, body {
    width: 1200px; height: 871px; overflow: hidden;
    background: var(--page);
    font-family: "Montserrat", Arial, sans-serif;
  }
  .canvas {
    position: relative; width: 1200px; height: 871px;
    display: flex; flex-direction: column; align-items: center; justify-content: center; gap: 30px;
  }
  .card {
    position: relative; width: 620px; height: 400px; overflow: hidden;
    border-radius: 4px;
    box-shadow: 0 14px 36px rgba(0,0,0,.55);
  }

  /* Contact side */
  .card--contact {
    background: linear-gradient(160deg, var(--card-grey) 0%, var(--card-charcoal) 55%, var(--card-black) 100%);
  }
  .card--contact .ornament {
    position: absolute; right: 0; top: 0; width: 340px; height: 400px;
    background: radial-gradient(ellipse at 60% 40%, rgba(127,182,224,.55) 0%, rgba(79,140,192,.25) 40%, rgba(0,0,0,0) 75%);
  }
  .brand {
    position: absolute; left: 40px; top: 48px;
    display: flex; align-items: center; gap: 10px;
    color: var(--text-light); font-weight: 700; font-size: 15px; letter-spacing: .04em;
    text-transform: uppercase;
  }
  .brand__square { width: 22px; height: 22px; background: var(--sky); }
  .name-band {
    position: absolute; left: 0; top: 130px; width: 100%; height: 66px;
    background: linear-gradient(180deg, var(--sky-pale), var(--sky) 50%, var(--sky-deep));
    border-top: 2px solid var(--card-black); border-bottom: 2px solid var(--card-black);
    padding: 10px 40px;
  }
  .name-band__name { color: var(--logo-panel); font-weight: 700; font-size: 24px; line-height: 1.1; }
  .name-band__role { color: var(--logo-panel); font-weight: 600; font-size: 12px; }
  .contact-list {
    position: absolute; left: 40px; bottom: 44px; list-style: none;
    color: var(--text-muted); font-size: 13px; line-height: 1.55; letter-spacing: .03em;
  }
  .contact-list b { display: inline-block; width: 18px; font-weight: 400; }
  .website {
    position: absolute; right: 60px; top: 232px;
    color: var(--text-light); font-weight: 700; font-size: 16px;
  }

  /* Logo side */
  .card--logo {
    background: linear-gradient(170deg, #1a1a1c 0%, var(--card-black) 60%, #050506 100%);
  }
  .card--logo .ornament {
    position: absolute; inset: 0;
    background:
      radial-gradient(ellipse at 25% 25%, rgba(90,92,96,.35) 0%, rgba(0,0,0,0) 55%),
      radial-gradient(ellipse at 75% 80%, rgba(90,92,96,.3) 0%, rgba(0,0,0,0) 55%);
  }
  .logo-band {
    position: absolute; left: 0; top: 150px; width: 100%; height: 100px;
    border-top: 2px solid #1f3a52; border-bottom: 2px solid #1f3a52;
  }
  .logo-band__fill {
    position: absolute; left: 0; top: 10px; width: 100%; height: 76px;
    background: linear-gradient(180deg, var(--sky-pale), var(--sky) 45%, var(--sky-deep));
  }
  .logo-panel {
    position: absolute; left: 50%; top: 50%; transform: translate(-50%, -50%);
    width: 320px; height: 140px;
    background: var(--logo-panel);
    border: 6px solid var(--sky-pale);
    display: flex; align-items: center; justify-content: center; gap: 14px;
  }
  .logo-panel__square { width: 40px; height: 40px; background: var(--text-light); flex: none; }
  .logo-panel__name {
    color: var(--text-light); font-weight: 700; font-size: 19px; line-height: 1.2;
    text-transform: uppercase; letter-spacing: .03em;
  }
</style>
</head>
<body>
<main class="canvas">

  <section class="card card--contact" aria-label="Business card, contact side">
    <div class="ornament" role="img" aria-label="Blue spot-gloss floral scroll ornament"></div>
    <div class="brand"><span class="brand__square"></span>Corin Vale Hospitality College</div>
    <div class="name-band">
      <p class="name-band__name">Tobin Marsh</p>
      <p class="name-band__role">Director</p>
    </div>
    <ul class="contact-list">
      <li><b>P</b>1300 615 737</li>
      <li><b>M</b>0455 817 296</li>
      <li>info@corinvale.example</li>
    </ul>
    <p class="website">www.corinvale.example</p>
  </section>

  <section class="card card--logo" aria-label="Business card, logo side">
    <div class="ornament" role="img" aria-label="Black-on-black spot UV floral scroll pattern"></div>
    <div class="logo-band"><div class="logo-band__fill"></div></div>
    <div class="logo-panel">
      <span class="logo-panel__square"></span>
      <p class="logo-panel__name">Corin Vale<br>Hospitality College</p>
    </div>
  </section>

</main>
</body>
</html>
```